Web Site Design for new Children's Book Series

We need a new web site design that complements a new children's book series that will be available next month. The main character is named 'Mippo Zelka Otter Cat Finch' and the story lines work through bullying issues for elementary age kids. This is a new design from scratch, but we have attached a collection of artwork from the new book series that the web site design should complement.

The scope of this project is only for the design / layout of the home page and one interior page for the web site.

Additional project details including the sitemap and example content are included in the attached document: 'Mippo Zelka Web Site.pdf'

We are open for questions and we look forward to seeing your creativity!
Updates

We have marked the project as guaranteed now!  We look forward to seeing your ideas and concepts!

Target Market(s)

Currently, there are two children’s books in the Mippo Zelka series aimed at elementary aged children. This collection is planned to grow over time. The goal of the web site is to provide information about the authors and the book series to elementary aged children (ages 3 to 12), their parents, and their school teachers and counselors.

Industry/Entity Type

Interior

Requirements
Must have
• The web site design should complement the attached artwork from the Mippo Zelka series. Overall, a full width design is desired that utilizes and open layout with lots of color.

The Mippo Zelka animal logo should be prominently placed. It is not necessary to retain the white background behind the logo.

The web site will be implemented as a responsive design using the Quill Scaffold framework and a standard 12 column grid.
Nice to have
• There are two themes in the books which should be incorporated into the web site design:

- Mippo Zelka uses the phrase “Way Cool” in describing various characters in the book and it is meant to build confidence and self esteem ... "you are way cool"

- An eagle feather is left behind as in “Zelka was here”. This eagle feature should be incorporated into the design in various locations.

```html
<!DOCTYPE html>
<html lang="en">
<head>
<meta charset="utf-8">
<title>Mippo Zelka – Home</title>
<link rel="stylesheet" href="https://fonts.googleapis.com/css2?family=Open+Sans:wght@400;600;700&family=Arvo:wght@400;700&family=Arimo:ital,wght@0,400;1,400&family=Noto+Serif:wght@700&display=swap">
<style>
:root{
  --blue:#19b9dc;
  --blue-dark:#13a2c4;
  --red:#f33f45;
  --green:#95bb1f;
  --orange:#ffa200;
  --cream:#f6e5dc;
  --brown:#5a3a1c;
  --ink:#3a3a3a;
  --muted:#777;
  --white:#fff;
}
*{box-sizing:border-box;margin:0;padding:0}
html,body{width:1200px;height:2663px;overflow:hidden}
body{font-family:"Open Sans",Arial,sans-serif;color:var(--ink);background:var(--white);position:relative}
section,header,footer{position:absolute;left:0;width:1200px}
.abs{position:absolute}

/* Header / hero */
.hero{top:0;height:570px;background:linear-gradient(180deg,var(--white) 0%,var(--white) 62%,var(--cream) 100%)}
.top-band{top:0;left:0;width:1200px;height:8px;background:var(--orange)}
.brand{left:168px;top:50px;display:flex;align-items:center;gap:14px;font-family:"Open Sans",Arial,sans-serif;font-weight:700;font-size:30px;line-height:1.05;color:var(--brown);width:220px}
.brand-dot{width:38px;height:38px;border-radius:50%;background:var(--brown);flex:none}
.nav{left:440px;top:64px;display:flex;list-style:none;font-size:16px}
.nav li{padding:6px 15px;border-radius:18px;color:#444;white-space:nowrap}
.nav li.active{background:var(--blue);color:var(--white)}
.hero-kicker{left:99px;top:314px;font-size:27px;font-weight:600;color:#f0742f;letter-spacing:.2px}
.hero-title{left:97px;top:362px;font-size:58px;font-weight:700;color:var(--blue);letter-spacing:1px}
.dots{left:99px;top:495px;display:flex;gap:12px}
.dots span{width:17px;height:17px;border-radius:50%;background:#bbb}
.dots span:first-child{background:#888}
.hero-photo{left:650px;top:120px;width:460px;height:440px;border-radius:8px;background:linear-gradient(180deg,#f3ede8 0%,#c7b59c 55%,#6b5a48 100%)}

/* Feature bands */
.band{color:var(--white)}
.band h2{font-family:"Arvo",Georgia,serif;font-weight:400;font-size:30px;letter-spacing:.5px;text-transform:uppercase}
.lead{font-size:16px;font-weight:700;line-height:27px}
.body-text{font-size:13.5px;line-height:23px}
.btn{display:inline-block;font-size:18px;padding:0 20px;height:47px;line-height:47px;color:var(--white);text-transform:uppercase}

.intro{top:570px;height:446px;background:var(--red)}
.intro .copy{left:86px;top:58px;width:568px}
.intro .lead{margin-top:16px}
.intro .body-text{margin-top:12px}
.intro .btn{margin-top:22px;background:var(--blue)}
.intro-art{left:700px;top:28px;width:415px;height:370px}

.release{top:1016px;height:498px;background:var(--green)}
.book{left:205px;top:77px;width:268px;height:377px;background:linear-gradient(160deg,#2e6a44 0%,#8bb6a4 45%,#5b9ab0 100%);box-shadow:6px 8px 14px rgba(0,0,0,.3)}
.release .copy{left:555px;top:98px;width:565px}
.release .lead{margin-top:20px}
.release .body-text{margin-top:12px}
.release .btn{margin-top:22px;background:var(--red)}

.authors{top:1514px;height:395px;background:var(--white)}
.author-photo{left:112px;top:61px;width:236px;height:272px;background:radial-gradient(ellipse at 50% 45%,#7a6a60 0%,#2e2a28 70%)}
.authors .copy{left:443px;top:80px;width:650px}
.authors h2{font-family:"Arvo",Georgia,serif;font-weight:400;font-size:30px;color:#555;text-transform:uppercase}
.authors .body-text{color:var(--muted);font-size:14px;line-height:23px;margin-top:14px}

.readers{top:1909px;height:303px;background:var(--orange);color:var(--white)}
.readers h2{position:absolute;top:48px;width:100%;text-align:center;font-family:"Arvo",Georgia,serif;font-weight:400;font-size:30px}
.quote-mark{font-family:"Noto Serif",Georgia,serif;font-weight:700;font-size:96px;line-height:1}
.quote-open{left:112px;top:92px}
.quote-close{left:1030px;top:187px}
.quote{left:165px;top:137px;width:915px;font-family:"Arimo",Arial,sans-serif;font-size:15px;line-height:37px}
.cite{left:0;top:222px;width:100%;text-align:center;font-weight:700;font-size:18px}

/* Footer */
.site-footer{top:2212px;height:451px;background:var(--blue);color:var(--white);font-family:"Arimo",Arial,sans-serif}
.site-footer h3{font-family:"Open Sans",Arial,sans-serif;font-weight:400;font-size:17px;text-transform:uppercase;letter-spacing:.3px}
.news{left:88px;top:54px;width:360px}
.news ul{list-style:none;margin-top:26px}
.news li{display:flex;gap:10px;margin-bottom:17px;font-size:13.5px;line-height:21px}
.news-icon{flex:none;width:18px;height:18px;margin-top:2px}
.news time{display:block;font-style:italic;font-size:12.5px}
.signup{left:496px;top:54px;width:230px}
.signup .field{display:block;width:226px;height:40px;border:1px solid var(--white);margin-top:10px;padding:0 12px;line-height:38px;font-size:13px}
.signup .field:first-of-type{margin-top:22px}
.signup .submit{display:block;margin:20px 0 0 145px;width:81px;height:33px;line-height:33px;text-align:center;background:var(--blue-dark);font-size:14px;text-transform:uppercase}
.mascot{left:842px;top:35px;width:226px;height:320px;border-radius:50% 50% 40% 40%;background:linear-gradient(180deg,#f2f2ea 0%,#9a5526 45%,#3b2313 100%)}
.legal{left:0;top:381px;width:1200px;height:70px;background:var(--blue-dark);font-size:13px}
.legal p{position:absolute;left:88px;top:26px}
.social{position:absolute;left:930px;top:20px;display:flex;gap:9px}
.social span{width:28px;height:28px;border-radius:50%;background:rgba(255,255,255,.4)}
</style>
</head>
<body>

<header class="hero">
  <div class="abs top-band"></div>
  <div class="abs brand"><span class="brand-dot"></span><span>Mippo<br>Zelka</span></div>
  <ul class="abs nav">
    <li class="active">Home</li>
    <li>About Authors</li>
    <li>Books</li>
    <li>Meet Characters</li>
    <li>Teachable Moments</li>
    <li>Contact</li>
  </ul>
  <p class="abs hero-kicker">CLARITAS EATIAM PROCESSUS DYCUS</p>
  <h1 class="abs hero-title">ANTEP SUERTUM</h1>
  <div class="abs dots"><span></span><span></span><span></span><span></span></div>
  <div class="abs hero-photo" role="img" aria-label="Photo of a young boy sitting on a stack of books, reading a picture book"></div>
</header>

<section class="band intro">
  <div class="abs copy">
    <h2>Introducing Mippo Zelka</h2>
    <p class="lead">Lorem ipsum dolor sit amet conse ctetur adipisicing elit, sed do eiusmod tempor incididunt ut labore et dolore magna aliquam. Ut enim ad minim veniam, quis nostrud exercitation ullamc.</p>
    <p class="body-text">Lorem ipsum dolor sit amet conse ctetur adipisicing elit, sed do eiusmod tempor in cididunt ut labore et dolore magna aliqua. Ut enim ad minim veniam, quis nostrud exercitation ullamco laboris nisi ut aliquip ex ea commodo consequat. Duis aute iru re dolor in reprehenderit in voluptate velit esse cillum dolore eu fugiat nulla.</p>
    <span class="btn">Read More</span>
  </div>
  <svg class="abs intro-art" viewBox="0 0 415 370" role="img" aria-label="Three round illustrations of the book characters outdoors">
    <defs><linearGradient id="scene" x1="0" y1="0" x2="0" y2="1"><stop offset="0" stop-color="#8fc7e0"/><stop offset=".55" stop-color="#7fae4a"/><stop offset="1" stop-color="#4f7a2c"/></linearGradient></defs>
    <circle cx="222" cy="100" r="98" fill="url(#scene)" stroke="#fff" stroke-width="3"/>
    <circle cx="95" cy="262" r="95" fill="url(#scene)" stroke="#fff" stroke-width="3"/>
    <circle cx="312" cy="262" r="100" fill="url(#scene)" stroke="#fff" stroke-width="3"/>
  </svg>
</section>

<section class="band release">
  <div class="abs book" role="img" aria-label="Cover of the new Mippo Zelka book with the characters on a dock"></div>
  <div class="abs copy">
    <h2>Our New Release</h2>
    <p class="lead">Lorem ipsum dolor sit amet conse ctetur adipisicing elit, sed do eiusmod tempor incididunt ut labore et dolore magna aliquam. Ut enim ad minim veniam, quis nostrud exercitation ullamc.</p>
    <p class="body-text">Lorem ipsum dolor sit amet conse ctetur adipisicing elit, sed do eiusmod tempor in cididunt ut labore et dolore magna aliqua. Ut enim ad minim veniam, quis nostrud exercitation ullamco laboris nisi ut aliquip ex ea commodo consequat. Duis aute iru re dolor in reprehenderit in voluptate velit esse cillum dolore eu fugiat nulla.</p>
    <span class="btn">Read More</span>
  </div>
</section>

<section class="authors">
  <div class="abs author-photo" role="img" aria-label="Portrait photo of the two authors"></div>
  <div class="abs copy">
    <h2>Author Visits</h2>
    <p class="body-text">Lorem ipsum dolor sit amet conse ctetur adipisicing elit, sed do eiusmod tempor incididu nt ut labore et dolore magna aliquam. Ut enim ad minim veniam, quis nostrud exercitatio n ullam dolor sit amet conse ctetur adipisicing elit, sed do eiusmod tempor.</p>
    <p class="body-text">Lorem ipsum dolor sit amet conse ctetur adipisicing elit, sed do eiusmod tempor incididunt ut la bore et dolore magna aliqua. Ut enim ad minim veniam, quis nostrud exercitation ullamco labori s nisi ut aliquip ex ea commodo consequat. Duis aute irure dolor in reprehenderit in voluptate ve lit esse cillum dolore eu fugiat nulla. dolor sit amet conse ctetur adipisicing elit.</p>
  </div>
</section>

<section class="readers">
  <h2>From Our Readers</h2>
  <span class="abs quote-mark quote-open">&ldquo;</span>
  <p class="abs quote">Claritas est etiam processus dynamicus, qui sequitur mutationem consuetudium lectorum. Mirum est notare quam li ttera gothica, quam nunc putamus parum claram, anteposuerit litterarum formas humanitatis per seacula.</p>
  <span class="abs quote-mark quote-close">&rdquo;</span>
  <p class="abs cite">- Dana Morrow, CEO</p>
</section>

<footer class="site-footer">
  <div class="abs news">
    <h3>Latest News</h3>
    <ul>
      <li><svg class="news-icon" viewBox="0 0 18 18" aria-hidden="true"><circle cx="9" cy="9" r="9" fill="#fff"/><rect x="5" y="5" width="8" height="8" fill="var(--blue)"/></svg><p>Linda : Vivamus sagittis lacus vel augue laor mfaucibus dolor auctor lorem Aenean.<time>Posted on March 14, 2013</time></p></li>
      <li><svg class="news-icon" viewBox="0 0 18 18" aria-hidden="true"><circle cx="9" cy="9" r="9" fill="#fff"/><rect x="5" y="5" width="8" height="8" fill="var(--blue)"/></svg><p>Linda : Vivamus sagittis lacus vel augue laor mfaucibus dolor auctor lorem Aenean.<time>Posted on March 14, 2013</time></p></li>
      <li><svg class="news-icon" viewBox="0 0 18 18" aria-hidden="true"><circle cx="9" cy="9" r="9" fill="#fff"/><rect x="5" y="5" width="8" height="8" fill="var(--blue)"/></svg><p>Linda : Vivamus sagittis lacus vel augue laor mfaucibus dolor auctor lorem Aenean.<time>Posted on March 14, 2013</time></p></li>
    </ul>
  </div>
  <div class="abs signup">
    <h3>Newsletter Signup</h3>
    <span class="field">Name</span>
    <span class="field">Email Id</span>
    <span class="submit">Submit</span>
  </div>
  <div class="abs mascot" role="img" aria-label="Illustration of the hound dog and eagle characters sitting together"></div>
  <div class="abs legal">
    <p>Mippo Zelka Enterprises &copy; 2014 &nbsp;Privacy Policy</p>
    <div class="social" aria-label="Social links"><span></span><span></span><span></span><span></span></div>
  </div>
</footer>

</body>
</html>
```